we are plumbers and builders.

one side with lantern installations mark fenwick 07700900417 01632960284 info@lanterninstallations.co.uk
other side
lantern construction
dean fenwick 07700900583
01632960284
info@lanternconstruction.co.uk

i don't want your bog standard logo id like something unusual maybe shape the card. i like black and silver,

```html
<!DOCTYPE html>
<html lang="en">
<head>
<meta charset="utf-8">
<title>Lantern – Round Business Cards</title>
<link href="https://fonts.googleapis.com/css2?family=Montserrat:wght@500;700&family=Roboto:wght@300&display=swap" rel="stylesheet">
<style>
  :root {
    --backdrop: #d4d0cb;
    --card-light: #ffffff;
    --card-dark: #1f1e1e;
    --brand-red: #e30613;
    --silver: #b3b3b3;
    --text-grey: #8a8a8a;
    --text-light: #d8d8d8;
  }
  * { margin: 0; padding: 0; box-sizing: border-box; }
  html, body {
    width: 1200px; height: 1200px; overflow: hidden;
    background: var(--backdrop);
  }
  .canvas { position: relative; width: 1200px; height: 1200px; }
  .card {
    position: absolute; top: 361px;
    width: 474px; height: 474px; border-radius: 50%;
    text-align: center;
  }
  .card--front { left: 72px; background: var(--card-light); }
  .card--back { left: 651px; background: var(--card-dark); }

  .wordmark {
    position: absolute; left: 64px; top: 114px;
    display: flex; align-items: center; gap: 16px;
  }
  .wordmark__ring {
    flex: none;
    width: 86px; height: 86px; border-radius: 50%;
    border: 8px solid var(--silver);
  }
  .wordmark__name {
    font-family: "Montserrat", sans-serif; font-weight: 500;
    color: var(--brand-red); text-align: left; line-height: 1;
  }
  .wordmark__name .line-main { display: block; font-size: 44px; letter-spacing: 1px; }
  .wordmark__name .line-sub { display: block; font-size: 15px; letter-spacing: 6.5px; margin-top: 7px; }

  .emblem {
    position: absolute; left: 144px; top: 51px;
    width: 186px; height: 186px; border-radius: 50%;
    border: 12px solid var(--silver);
    display: flex; flex-direction: column; align-items: center; justify-content: center;
    font-family: "Montserrat", sans-serif; font-weight: 500; color: var(--brand-red);
    line-height: 1;
  }
  .emblem .line-main { font-size: 28px; letter-spacing: 1px; }
  .emblem .line-sub { font-size: 11px; letter-spacing: 3px; margin-top: 6px; }

  .person {
    position: absolute; left: 0; right: 0; top: 296px;
    font-family: "Montserrat", sans-serif; font-weight: 700;
    font-size: 25px; letter-spacing: 1.5px; color: var(--brand-red);
    text-transform: uppercase;
  }
  .contact-icons {
    position: absolute; left: 193px; top: 349px;
    width: 89px; height: 23px; border: 1.5px solid var(--brand-red); border-radius: 12px;
    display: flex; align-items: center; justify-content: space-around; padding: 0 8px;
  }
  .contact-icons svg { width: 13px; height: 13px; }
  .contact-details {
    position: absolute; left: 0; right: 0; top: 380px;
    font-family: "Roboto", sans-serif; font-weight: 300;
    font-size: 15.5px; line-height: 21px; color: var(--text-grey);
  }
  .card--back .contact-details { color: var(--text-light); }
</style>
</head>
<body>
<main class="canvas">

  <section class="card card--front">
    <div class="wordmark">
      <span class="wordmark__ring"></span>
      <span class="wordmark__name">
        <span class="line-main">LANTERN</span>
        <span class="line-sub">INSTALLATIONS</span>
      </span>
    </div>
    <h2 class="person">Mark Fenwick</h2>
    <div class="contact-icons" aria-hidden="true">
      <svg viewBox="0 0 16 16"><rect x="4.5" y="1" width="7" height="14" rx="1.2" fill="none" stroke="#e30613" stroke-width="1.5"/><circle cx="8" cy="12.5" r="0.9" fill="#e30613"/></svg>
      <svg viewBox="0 0 16 16"><path d="M3 2.5l2.5-.5 1.5 3.5-1.8 1.2a8 8 0 0 0 4 4l1.2-1.8 3.5 1.5-.5 2.5C8 13.5 2.5 8 3 2.5z" fill="#e30613"/></svg>
      <svg viewBox="0 0 16 16"><rect x="1.5" y="4" width="13" height="9" fill="none" stroke="#e30613" stroke-width="1.5"/><path d="M1.5 4l6.5 5 6.5-5" fill="none" stroke="#e30613" stroke-width="1.5"/></svg>
    </div>
    <p class="contact-details">07700900417&nbsp; | &nbsp;01632960284<br>info@lanterninstallations.co.uk</p>
  </section>

  <section class="card card--back">
    <div class="emblem">
      <span class="line-main">LANTERN</span>
      <span class="line-sub">CONSTRUCTION</span>
    </div>
    <h2 class="person">Dean Fenwick</h2>
    <div class="contact-icons" aria-hidden="true">
      <svg viewBox="0 0 16 16"><rect x="4.5" y="1" width="7" height="14" rx="1.2" fill="none" stroke="#e30613" stroke-width="1.5"/><circle cx="8" cy="12.5" r="0.9" fill="#e30613"/></svg>
      <svg viewBox="0 0 16 16"><path d="M3 2.5l2.5-.5 1.5 3.5-1.8 1.2a8 8 0 0 0 4 4l1.2-1.8 3.5 1.5-.5 2.5C8 13.5 2.5 8 3 2.5z" fill="#e30613"/></svg>
      <svg viewBox="0 0 16 16"><rect x="1.5" y="4" width="13" height="9" fill="none" stroke="#e30613" stroke-width="1.5"/><path d="M1.5 4l6.5 5 6.5-5" fill="none" stroke="#e30613" stroke-width="1.5"/></svg>
    </div>
    <p class="contact-details">07700900583&nbsp; | &nbsp;01632960284<br>info@lanternconstruction.co.uk</p>
  </section>

</main>
</body>
</html>
```